Enhance the web site presence of Kolrith Global Limited

Upgrade the current web site www.kolrithpanel.com to share with the audience our current plan and future developments of our company. I have created a worksheet which shows all the pages that I like to have. The home page in English, Japanese and Chinese is hyperlinked to the various pages. Under the product, we should allow the user to select "single sided PCB or double sided PCB". The translation of the contents of the pages with Japanese is not complete but the English and Chinese are complete. You can download the briefing and photos in the dropbox files below;

https://www.sharelocker.net/sh/xk4trw92mpd3ab1/BBQm_Lp841zzPq2Rw7KtYnHjEa?dl=0

Target Market(s)

Electronic companies

Industry/Entity Type

Electronic

Coding

Coded - Design and coding required

Number of Pages Required

5+ page

Font styles to use
Sans Serif

Colors
00a990
0353a1
33b8a4

Requirements
Must have
• Get a sense of confidence on our company's integrity and capability to deliver the highest quality PCBs with the most competitive prices and best services. A sense of elegance is essential as we DON'T treat profits as the number one goal. Our number goal is to do the RIGHT things right. Having a mixture of our company photos will be appropriate.

```html
<!DOCTYPE html>
<html lang="en">
<head>
<meta charset="utf-8">
<title>Our Products – Kolrith Global Limited</title>
<link href="https://fonts.googleapis.com/css2?family=Roboto:wght@400;500;700&family=Montserrat:wght@600;700&display=swap" rel="stylesheet">
<style>
:root{
  --teal:#00a990;
  --teal-light:#33b8a4;
  --blue:#0353a1;
  --navy:#0b2f5c;
  --topbar:#0a5a4c;
  --ink:#333;
  --muted:#666;
  --line:#e5e5e5;
  --page:#f3f3f3;
}
*{margin:0;padding:0;box-sizing:border-box}
html,body{width:1200px;height:2628px;overflow:hidden}
body{font-family:'Roboto',sans-serif;color:var(--ink);background:var(--page);font-size:13px;position:relative}
.topbar{height:28px;background:var(--topbar);color:#fff;font-size:11px;display:flex;align-items:center;gap:22px;padding:0 60px}
.topbar span{display:flex;align-items:center;gap:6px}
.header{height:60px;background:#fff;display:flex;align-items:center;padding:0 60px;border-bottom:1px solid var(--line)}
.brand{display:flex;align-items:center;gap:10px;font-family:'Montserrat',sans-serif;font-weight:700;font-size:24px;color:var(--teal)}
.brand .mark{width:14px;height:14px;background:var(--teal)}
.nav{margin-left:auto;display:flex;align-items:center;gap:4px;font-size:11px;font-weight:500}
.nav a{padding:22px 13px;color:#222;text-decoration:none}
.nav a.active{background:var(--teal);color:#fff}
.lang{margin-left:14px;font-size:11px;color:#555}
.login{margin-left:14px;background:var(--teal);color:#fff;padding:7px 14px;font-size:11px;border-radius:2px}
.hero{height:332px;background:linear-gradient(180deg,#2b4a45,#1c2f2c 60%,#3a5a52);display:flex;flex-direction:column;align-items:center;justify-content:center;color:#fff}
.hero h1{font-family:'Montserrat',sans-serif;font-size:40px;font-weight:600}
.hero p{font-size:11px;margin-top:8px;opacity:.85}
.tabs{display:flex;justify-content:center;margin-top:180px}
.tab{padding:12px 34px;font-size:12px;border:1px solid #ccc;background:#fff;color:#555}
.tab.active{border-bottom:2px solid var(--teal);color:#222}
.card{width:968px;margin:46px auto 0;background:#fff;border:1px solid var(--line);padding:28px 20px 40px}
.intro{display:flex;gap:26px}
.photo{width:370px;height:300px;background:linear-gradient(135deg,#7fa7b5,#c9d6da 50%,#5f7d88);flex:none}
.intro h2{font-family:'Montserrat',sans-serif;font-size:27px;line-height:1.25;color:#111;margin:40px 0 18px}
.intro p{font-size:12px;line-height:1.55;color:var(--muted);margin-bottom:12px}
table{width:100%;border-collapse:collapse;margin-top:22px;font-size:11px}
th{background:var(--teal);color:#fff;text-align:left;padding:15px 18px;font-weight:500;font-size:12px}
td{padding:0 18px;height:44px;border-bottom:1px solid var(--line);color:#444}
td:first-child{width:360px}
.footer{position:absolute;top:2250px;left:0;width:1200px;height:378px;background:var(--navy);color:#fff}
.f-brand{position:absolute;left:120px;top:140px;text-align:center;width:260px}
.f-brand .brand{color:#fff;justify-content:center;font-size:34px}
.f-brand .brand .mark{background:#fff}
.f-brand p{font-size:11px;margin-top:14px}
.col{position:absolute;top:110px;font-size:11px}
.col h3{font-size:14px;font-weight:500;margin-bottom:14px;letter-spacing:.5px}
.col li{list-style:none;line-height:23px;display:flex;align-items:center;gap:7px}
.col li::before{content:"";width:4px;height:4px;background:var(--teal-light);border-radius:50%}
.links{left:530px}
.contact{left:800px}
.contact li::before{display:none}
.dot{width:10px;height:10px;border-radius:50%;background:var(--teal-light);flex:none}
.totop{position:absolute;left:1128px;top:2582px;width:30px;height:30px;border-radius:50%;background:var(--teal);display:flex;align-items:center;justify-content:center}
</style>
</head>
<body>
<div class="topbar">
  <span><svg width="12" height="9" viewBox="0 0 12 9"><rect x=".5" y=".5" width="11" height="8" fill="none" stroke="#fff"/><path d="M.5 .5 6 5l5.5-4.5" fill="none" stroke="#fff"/></svg>sales@kolrithpanel.com</span>
  <span><svg width="10" height="10" viewBox="0 0 10 10"><path d="M2 0h2l1 3-1.5 1a6 6 0 0 0 2.5 2.5L7 5l3 1v2a2 2 0 0 1-2 2A8 8 0 0 1 0 2a2 2 0 0 1 2-2z" fill="#fff"/></svg>(852) 3946 2718</span>
</div>
<header class="header">
  <div class="brand"><span class="mark"></span>KOLRITH</div>
  <nav class="nav">
    <a href="#">HOME</a><a href="#" class="active">PRODUCTS</a><a href="#">OUR FACILITIES</a><a href="#">CUSTOMER</a><a href="#">NEWS</a><a href="#">QUOTES</a><a href="#">CONTACT US</a>
  </nav>
  <span class="lang">EN ▾</span>
  <span class="login">LOGIN</span>
</header>
<section class="hero" role="img" aria-label="Factory production floor background photo">
  <h1>Our Products</h1>
  <p>Home / Products</p>
</section>
<div class="tabs"><div class="tab">Single Sided PCBs</div><div class="tab active">Double Sided/Multi Layered PCBs</div></div>
<main class="card">
  <div class="intro">
    <div class="photo" role="img" aria-label="Technician inspecting circuit boards at a production line"></div>
    <div>
      <h2>Double layered and multi-layered<br>printed circuit boards</h2>
      <p>We are offering two layered and multi-layered circuit boards for our customers through our strategically approved printed circuit boards manufacturers.<br>With our over 20 years of experience, we work with a number of strategically approved manufacturers in delivering 100% quality guaranteed printed circuit boards for our customers.</p>
      <p>We perform comprehensive quality and environmental audit of our manufacturers on quarterly and annual basis.</p>
    </div>
  </div>
  <table>
    <tr><th>Item</th><th>Description</th></tr>
    <tr><td>Layers</td><td>2–16</td></tr>
    <tr><td>Laminate</td><td>CEM-1, CEM-3, FR-4, High Tg, Halogen free, Aluminium base, Ceramic, PTFE, High-frequency etc.</td></tr>
    <tr><td>Flammability</td><td>UL 94V-0</td></tr>
    <tr><td>Board thickness</td><td>0.40–6.0mm</td></tr>
    <tr><td>Min. conductor width/spacing</td><td>0.075mm</td></tr>
    <tr><td>Cu thickness on inner layer</td><td>Max. 4 OZ</td></tr>
    <tr><td>Finish Cu thickness in hole wall</td><td>Max. 4 OZ</td></tr>
    <tr><td>Via/PTH, min</td><td>&gt; 18 μm</td></tr>
    <tr><td>Min. drill hole diameter</td><td>0.2mm/0.0mm</td></tr>
    <tr><td>Plating aspect ratio</td><td>8:1mm</td></tr>
    <tr><td>Tolerance of hole position</td><td>±0.1</td></tr>
    <tr><td>Tolerance of hole diameter</td><td>±0.05mm</td></tr>
    <tr><td>Solder mask</td><td>LPI ink/Photo-imageable/Others</td></tr>
    <tr><td>Color of solder mask</td><td>LPI/Thermocuring/UV</td></tr>
    <tr><td>Hardness of solder mask</td><td>Green/Red/Blue/Black/White/Etc</td></tr>
    <tr><td>Min spacing of soldermask</td><td>&gt;6H</td></tr>
    <tr><td>Ability of blank hole with Vill</td><td>0.08mm</td></tr>
    <tr><td>Outline tolerance</td><td>0.50mm–6.00mm</td></tr>
    <tr><td>Surface finishing</td><td>Punch ±0.10mm / CNC Routing ±0.10mm</td></tr>
    <tr><td>V-cut angle</td><td>ENIG, Ni 3-5μm, Au 0.05μm, HASL, OSP</td></tr>
    <tr><td>Chamfer angle</td><td>20°/30°/45°/60°</td></tr>
    <tr><td>E-Test</td><td>20°/30°/45°/60°</td></tr>
    <tr><td>Outgoing Standard</td><td>Max. test point: 16384<br>IPC-A-600H Class 2 or refer to customer's requirement</td></tr>
  </table>
</main>
<footer class="footer">
  <div class="f-brand">
    <div class="brand"><span class="mark"></span>KOLRITH</div>
    <p>Copyright © 2016, Kolrith Global Limited<br>All Rights Reserved</p>
  </div>
  <div class="col links">
    <h3>USEFUL LINKS</h3>
    <ul><li>Home</li><li>Products</li><li>Our Facilities</li><li>Customer</li><li>News</li><li>Quotes</li><li>Contact Us</li></ul>
  </div>
  <div class="col contact">
    <h3>CONTACT US</h3>
    <ul>
      <li><span class="dot"></span>Kolrith Global Limited</li>
      <li style="padding-left:17px">18/F Lumen Centre</li>
      <li style="padding-left:17px">27 Harbour Crescent</li>
      <li style="padding-left:17px">Tsuen Wan, N.T., Hong Kong</li>
      <li><span class="dot"></span>Telephone: (852) 3946 2718</li>
      <li><span class="dot"></span>Fax: (852) 3946 2719</li>
      <li><span class="dot"></span>Email: sales@kolrithpanel.com</li>
    </ul>
  </div>
</footer>
<div class="totop"><svg width="12" height="8" viewBox="0 0 12 8"><path d="M1 7l5-5 5 5" fill="none" stroke="#fff" stroke-width="2"/></svg></div>
</body>
</html>
```